One Page Sales Flyer for Wireless Survey- Computer Hardware

I want a designer to create a one page 4 color sales slick to be given to our sales team to sell to the end customers. I would like a visual picture of a heat map so zavvix "heat map wireless" to get an idea of how that image should look.

```html
<!DOCTYPE html>
<html lang="en">
<head>
<meta charset="utf-8">
<title>Wireless Site Survey Flyer</title>
<link href="https://fonts.googleapis.com/css2?family=Fira+Sans:wght@300;400;600;700&display=swap" rel="stylesheet">
<style>
  :root {
    --backdrop: #d4d5d7;
    --paper: #ffffff;
    --brand-blue: #4aa3db;
    --ink: #3a3a3a;
    --ink-soft: #555555;
    --map-light: #e9eef2;
    --map-mid: #c9d9e4;
  }
  * { margin: 0; padding: 0; box-sizing: border-box; }
  html, body { width: 1200px; height: 1000px; overflow: hidden; background: var(--backdrop); }
  body { font-family: "Fira Sans", Arial, sans-serif; color: var(--ink); position: relative; }

  .flyer { position: absolute; left: 247px; top: 43px; width: 706px; height: 914px; background: var(--paper); }
  .top-band { position: absolute; left: 0; top: 0; width: 706px; height: 64px; background: var(--brand-blue); }

  .city-illustration {
    position: absolute; left: 306px; top: 64px; width: 400px; height: 338px;
    background: linear-gradient(160deg, var(--map-light) 0%, var(--map-mid) 70%, #8fc3e6 100%);
    clip-path: polygon(0 0, 400px 0, 400px 338px, 300px 318px, 180px 290px, 90px 268px, 40px 252px, 0 238px);
  }

  .kicker { position: absolute; left: 23px; top: 90px; font-size: 21px; font-weight: 300; line-height: 28px; color: var(--ink); letter-spacing: 0.3px; }
  .wifi-icon { position: absolute; left: 56px; top: 152px; }
  .title { position: absolute; left: 23px; top: 173px; font-size: 47px; font-weight: 600; line-height: 44px; color: var(--brand-blue); letter-spacing: 0.3px; }

  .section { position: absolute; left: 23px; width: 470px; }
  .section h2 { font-size: 16px; font-weight: 600; color: var(--brand-blue); line-height: 21px; margin-bottom: 7px; }
  .section p, .section li { font-size: 13px; line-height: 16.4px; color: var(--ink); letter-spacing: 0.25px; }
  .section b { font-weight: 600; }
  .what { top: 313px; }
  .why { top: 485px; }
  .use { top: 599px; }
  .use ol { list-style: none; }
  .use li { padding-left: 14px; text-indent: -14px; }

  .footnote { position: absolute; left: 23px; top: 793px; font-size: 8px; color: var(--ink-soft); }

  .targets-cap { position: absolute; left: 502px; top: 447px; width: 180px; height: 13px; background: var(--brand-blue); }
  .targets-title { position: absolute; left: 502px; top: 466px; width: 180px; text-align: center; font-size: 19px; font-weight: 600; line-height: 21px; color: var(--brand-blue); }
  .targets-list { position: absolute; left: 502px; top: 514px; width: 180px; height: 288px; background: var(--brand-blue); list-style: none; padding: 14px 0 0 21px; }
  .targets-list li { font-size: 13px; font-weight: 600; color: #fff; line-height: 26px; letter-spacing: 0.2px; }

  .brand-mark { position: absolute; left: 24px; top: 816px; width: 76px; height: 76px; border: 3px solid var(--brand-blue); border-radius: 6px; display: flex; align-items: center; justify-content: center; font-size: 14px; font-weight: 600; color: var(--brand-blue); }
  .footer-band { position: absolute; left: 111px; top: 816px; width: 595px; height: 76px; background: var(--brand-blue); color: #fff; }
  .website { position: absolute; left: 104px; top: 50px; font-size: 12px; font-weight: 600; letter-spacing: 2.5px; }
  .email { position: absolute; right: 23px; top: 13px; font-size: 14px; }
  .phone { position: absolute; right: 23px; top: 33px; font-size: 30px; font-weight: 600; letter-spacing: 0.8px; }
</style>
</head>
<body>
<main class="flyer">
  <div class="top-band"></div>
  <div class="city-illustration" role="img" aria-label="Illustrated city map with streets, buildings, people and wifi signal icons beside a river"></div>

  <p class="kicker">Increase Hardware<br>and Service Spend with</p>
  <svg class="wifi-icon" width="30" height="22" viewBox="0 0 30 22" aria-hidden="true">
    <g fill="none" stroke="#4aa3db" stroke-width="3" stroke-linecap="round">
      <path d="M3 9 A17 17 0 0 1 27 9"/>
      <path d="M8 14 A10 10 0 0 1 22 14"/>
    </g>
    <circle cx="15" cy="19" r="2.5" fill="#4aa3db"/>
  </svg>
  <h1 class="title">WIRELESS<br>SITE SURVEY</h1>

  <section class="section what">
    <h2>What is a WIRELESS SITE SURVEY<br>or HEAT MAP?</h2>
    <p>A wireless site survey is a <b>compilation of reports showing<br>a visual&nbsp; representation of health of your wireless network.</b><br>This does not only show how strong or weak a wireless signal is<br>in any location it also helps aid in channel and placement to<br>ensure maximum stable data rates are archived even where<br>the single appears strong.</p>
  </section>

  <section class="section why">
    <h2>Why do customers need a SITE SURVEY?</h2>
    <p>Any variety of factors can contribute to an <b>unhealthy wireless network</b><br>(electrical, motors, etc) and traditional methods that use only blueprints<br>and a computer program to show signal strength have shown to be<br><b>ineffective.</b></p>
  </section>

  <section class="section use">
    <h2>Why should they use you?</h2>
    <ol>
      <li>1. <b>42% of businesses report some issues with wireless connectivity and<br>acknowledge its effect on the bottom line*</b></li>
      <li>2. Most of these problems are solved through either fine tuning the<br>current equipment (managed services) or purchasing new<br>equipment (incremental sales) of which you can provide both</li>
      <li>3. Being a one-stop shop for all your customer's IT need prevents them<br>from needing additional vendors</li>
      <li>4. The increase of <b>IoT (Internet of Things)</b> and <b>BYOD (Bring Your Own<br>Device)</b></li>
    </ol>
  </section>

  <p class="footnote">*Netwire.com. "Connectivity in the Modern Enterprise". June 2017</p>

  <div class="targets-cap"></div>
  <h2 class="targets-title">TARGET<br>CUSTOMERS</h2>
  <ul class="targets-list">
    <li>DISTRIBUTORS</li>
    <li>WAREHOUSES</li>
    <li>SLED</li>
    <li>K-12</li>
    <li>MEDICAL/ HOSPITALS</li>
    <li>ENTERPRISE F1000</li>
    <li>SPORTS VENUES</li>
    <li>STADIUMS</li>
    <li>HOTELS</li>
    <li>RETAIL STORES</li>
  </ul>

  <div class="brand-mark">Corvane</div>
  <footer class="footer-band">
    <span class="website">WWW.CORVANE.COM</span>
    <span class="email">info@corvane.com</span>
    <span class="phone">555 014 2290</span>
  </footer>
</main>
</body>
</html>
```